Redesign Australian netball site

Existing website needs a new look and feel - http://kelvalecourts.com.au/
We require a homepage design that contains 3 sections: Chatterly feed, Recent Articles and Sponsors.
We also require a subpage design showing a main content area and a right hand sidebar (containing panels for login, chatterly feed, articles and sponsors)
Updates

Hopefully the updated brief provides more information now but if there are further questions then feel free to email me at ts@brightwharf.com.au

Reason: To allow additional submissions and design tweaks

Target Market(s)

The site needs to target parents of younger players, older players themselves and sponsors.

Requirements
Must have
• Header must contain:
1. current logo from http://kelvalecourts.com.au/
2. The slogan "Fun, Fitness, Fair Competition - Play Netball"
3. A space for a Platinum Sponsor (see current site)

Top level navigation should be:
1. Seniors
2. Juniors
3. Zippets
4. Sponsors
5. Special Offers
6. About Us
7. Umpires

```html
<!DOCTYPE html>
<html lang="en">
<head>
<meta charset="utf-8">
<title>Kelvale Netball – Home</title>
<link href="https://fonts.googleapis.com/css2?family=Oswald:wght@400;500;600&family=Open+Sans:wght@400;600;700&display=swap" rel="stylesheet">
<style>
:root{
  --navy:#1d3f7a;
  --navy-dark:#142d59;
  --pink:#e2237a;
  --sky:#bfe4f4;
  --sky-light:#e8f6fc;
  --text:#333;
  --muted:#666;
  --rule:#d5dde4;
  --footer:#eef6fa;
}
*{box-sizing:border-box;margin:0;padding:0}
html,body{width:820px;height:1200px;overflow:hidden}
body{font-family:"Open Sans",Arial,sans-serif;color:var(--text);font-size:9px;line-height:1.35;
  background:linear-gradient(180deg,var(--sky) 0,var(--sky-light) 330px,#fff 420px)}
.page{width:660px;margin:0 auto;position:relative}
.site-header{height:92px;display:flex;justify-content:space-between;align-items:center}
.brand{display:flex;align-items:center;gap:8px;font-family:"Oswald",sans-serif;font-weight:600;font-size:20px;color:var(--navy)}
.brand-dot{width:46px;height:46px;border-radius:50%;background:var(--navy)}
.platinum{display:flex;align-items:center;gap:8px;font-size:10px;color:var(--navy);font-weight:600;text-align:right}
.platinum-box{width:96px;height:50px;background:#fff;border:1px solid var(--rule);color:var(--navy);font-family:"Open Sans",sans-serif;font-size:14px;font-weight:700;display:flex;align-items:center;justify-content:center}
.main-nav{height:28px;background:linear-gradient(var(--navy),var(--navy-dark));border-radius:4px;display:flex;align-items:stretch;padding-left:10px}
.main-nav a{color:#fff;text-decoration:none;font-family:"Oswald",sans-serif;font-size:11px;letter-spacing:.5px;padding:0 16px;display:flex;align-items:center}
.main-nav a.is-active{background:var(--pink)}
.hero{margin-top:10px;height:160px;background:linear-gradient(135deg,#7fb0d3,#c9a2b8 55%,#3c5e97);border:3px solid #fff;box-shadow:0 1px 4px rgba(0,0,0,.2)}
.slogan{font-family:"Oswald",sans-serif;font-weight:600;font-size:25px;color:var(--navy);text-align:center;padding:10px 0 8px;text-transform:uppercase}
.hot-press{display:flex;height:32px;background:#e5e9ec;border:1px solid var(--rule)}
.hot-press h2{font-family:"Oswald",sans-serif;font-size:14px;font-weight:500;color:#fff;background:#7d8b95;padding:0 22px 0 12px;display:flex;align-items:center;text-transform:uppercase;white-space:nowrap;clip-path:polygon(0 0,90% 0,100% 50%,90% 100%,0 100%)}
.hot-press p{padding:4px 12px;font-size:8.5px;color:var(--muted);align-self:center}
.hot-press b{color:var(--navy)}
.columns{display:grid;grid-template-columns:1fr 1fr 1fr;gap:18px;margin-top:14px;height:668px}
.col-title{font-family:"Oswald",sans-serif;font-weight:500;font-size:16px;color:var(--navy);text-align:center;text-transform:uppercase;padding-bottom:6px;border-bottom:2px solid var(--navy);margin-bottom:10px}
.article{margin-bottom:14px}
.article h3{font-family:"Oswald",sans-serif;font-weight:500;font-size:13px;color:var(--navy);line-height:1.2;margin-bottom:5px}
.article-body{display:flex;gap:7px}
.thumb{width:78px;height:62px;flex:none;background:linear-gradient(135deg,#e6a3c0,#5b7fb6)}
.article p{font-size:8px;color:var(--muted)}
.more{color:var(--pink);font-weight:700}
.feed-post{border-bottom:1px solid var(--rule);padding-bottom:8px;margin-bottom:8px;font-size:8px;color:var(--muted)}
.feed-post .photo{height:78px;margin:5px 0;background:linear-gradient(135deg,#9fc4e0,#d7b3c6)}
.feed-post small{display:block;color:#999;font-size:7px;margin-top:2px}
.sponsor-group{margin-bottom:14px}
.sponsor-group h4{font-family:"Oswald",sans-serif;font-weight:500;font-size:13px;color:var(--navy);margin-bottom:6px}
.sponsor-box{display:flex;align-items:center;justify-content:center;font-weight:700;font-size:14px;color:var(--navy);border:1px solid var(--rule);background:#fff;height:52px;margin-bottom:6px}
.sponsor-box.lead{height:90px;font-size:18px}
.sponsor-pair{display:flex;gap:6px}
.sponsor-pair .sponsor-box{flex:1;font-size:11px}
.site-footer{background:var(--footer);border-top:3px solid var(--navy);padding:10px 12px;display:grid;grid-template-columns:1fr 1fr 1fr;gap:18px;height:82px}
.site-footer h5{font-family:"Oswald",sans-serif;font-weight:500;font-size:11px;color:var(--navy);text-transform:uppercase;margin-bottom:3px}
.site-footer ul{list-style:none;font-size:7.5px;color:var(--muted);line-height:1.45}
.site-footer li::before{content:"› ";color:var(--pink)}
.site-footer p{font-size:7.5px;color:var(--muted)}
.contact{display:flex;justify-content:space-between;align-items:flex-end}
.social{display:flex;gap:4px}
.social span{width:14px;height:14px;border-radius:50%;background:var(--navy)}
.copyright{text-align:center;font-size:7.5px;color:var(--muted);padding-top:8px}
</style>
</head>
<body>
<div class="page">
  <header class="site-header">
    <div class="brand"><span class="brand-dot"></span>Kelvale Netball</div>
    <div class="platinum"><span>Platinum<br>Sponsor</span><div class="platinum-box">Tallmere</div></div>
  </header>
  <nav class="main-nav">
    <a href="#">SENIORS</a><a href="#" class="is-active">JUNIORS</a><a href="#">ZIPPETS</a><a href="#">SPONSORS</a><a href="#">SPECIAL OFFERS</a><a href="#">ABOUT US</a><a href="#">UMPIRES</a>
  </nav>
  <div class="hero" role="img" aria-label="Netball players competing for the ball on court"></div>
  <h1 class="slogan">Fun, Fitness, Fair Competition - Play Netball</h1>
  <section class="hot-press">
    <h2>Hot of the Press</h2>
    <p>Winter season grading days are now set. Check your team list and court times before the first round begins... <b>read more</b></p>
  </section>

  <div class="columns">
    <section>
      <h2 class="col-title">Recent Articles</h2>
      <article class="article">
        <h3>Jenna Corrow Clinic for KN Members</h3>
        <div class="article-body">
          <div class="thumb" role="img" aria-label="Coach leading a junior clinic"></div>
          <p>Saturday 11th May. Cost $40 per child, includes training and a signed ball. Registration opens online now, places are limited. <span class="more">more</span></p>
        </div>
      </article>
      <article class="article">
        <h3>Kelvale ill off to a Flying Start!</h3>
        <div class="article-body">
          <div class="thumb" role="img" aria-label="Team celebrating a win"></div>
          <p>Our under 11 team opened the season with a strong win and great spirit. Well done to every player and coach. <span class="more">more</span></p>
        </div>
      </article>
      <article class="article">
        <h3>How Much Is Too Much? Overtraining in Children</h3>
        <div class="article-body">
          <div class="thumb" role="img" aria-label="Young player resting on the bench"></div>
          <p>By Tess Hallam, physio. Young players need rest as much as training. Here are signs to watch for and simple tips for parents. <span class="more">more</span></p>
        </div>
      </article>
    </section>

    <section>
      <h2 class="col-title">Chatterly Feed</h2>
      <div class="feed-post">Sorry for the late notice, all courts are closed today due to wet weather. Games will be replayed later in the season.<small>2 hours ago</small></div>
      <div class="feed-post">Who's keeping match ready over the school holidays? Senior fitness sessions run Tuesday nights at 6pm.
        <div class="photo" role="img" aria-label="Players at a fitness session"></div><small>Yesterday</small></div>
      <div class="feed-post">Junior uniforms are now available from the club shop. Please bring your sizing form.<small>3 days ago</small></div>
      <div class="feed-post">Junior training lists are now up. If your child is not listed, contact the junior coordinator by email.<small>5 days ago</small></div>
    </section>

    <section>
      <h2 class="col-title">Sponsors</h2>
      <div class="sponsor-group"><h4>Platinum Sponsor</h4><div class="sponsor-box lead">Tallmere</div></div>
      <div class="sponsor-group"><h4>Gold Sponsors</h4><div class="sponsor-box">Bandora</div></div>
      <div class="sponsor-group"><h4>Silver Sponsors</h4><div class="sponsor-box">Blossomday</div><div class="sponsor-box">Harbour Physio</div></div>
      <div class="sponsor-group"><h4>Bronze Sponsors</h4>
        <div class="sponsor-pair"><div class="sponsor-box">Coastline</div><div class="sponsor-box">Maison Verre</div></div>
      </div>
    </section>
  </div>

  <footer class="site-footer">
    <div><h5>Club Information</h5><ul><li>The Committee</li><li>Privacy Policy</li><li>Join Our Club</li><li>Contact Us</li></ul></div>
    <div><h5>Members Area</h5><ul><li>2013 Junior Teams</li><li>2013 Senior Teams</li><li>2013 Draw</li><li>2013 Results</li></ul></div>
    <div><h5>Contact Us</h5>
      <div class="contact"><p>Kelvale Netball Club<br>PO Box 12<br>Kelvale</p><div class="social"><span></span><span></span><span></span></div></div>
    </div>
  </footer>
  <p class="copyright">© 2013 kelvalecourts.com.au | Privacy Policy &amp; Disclaimer</p>
</div>
</body>
</html>
```